ONE PAGE WEB DESIGN NEEDED for Finance Company

We need a web design (ONE PAGE DESIGN ONLY) for a new finance website called Brightwell Lending. Brightwell Lending helps customers get the right loan, whether its a home loan, investment loan, business loan etc.

You are required to come up with just the homepage design. Professionalism and quality is the key factors in the successful design.

Here are a few design questions to help you out:

-
What information should be used on the page?
Ive provided a document which outlines all the information needed to put on homepage (attached to the brief - called brightwell_page_info). Also see the Must Have section below on this brief.

-
What links should appear in the navigation/footer?:
The navigation should provide links to the following pages (NOTE: services link has subcategories):
1 Homepage
2 Services
- Home loans
- Investment loans
- Refinancing loans
- Business loans
3 About Us
4 FAQ
5 Contact Us

-
What colors should be used in the design?
Our company colors - Cyan: #2EADE3, Blue: #004B70, White. Feel free to submit designs with slight variations if you feel it improves the design.

-
What should the layout of the page be?
This is up to you to come up with - we are open to different layouts for the page design (as long as they capture the information effectively and making it easy to understand).

Target Market(s)

Potential Home owners, Families and Business Owners

Industry/Entity Type

Business

Requirements
Must have
• - Must contain our logo (attached as PNG and Illustrator file)
- Winning designer must supply a Photoshop file (PSD) that will allow us.
Nice to have
• - Should include photos/images of families, professional groups, tradespeople etc (you can use stock photos from PixQuarry and I will purchase them once you are selected as the winning design)
- Link to a loan calculator somewhere on front page with a button 'Find out how much you could borrow' (or maybe even try adding a loan calculator to the homepage if you think this would look good)
- Page should have a main headline "Finding the right loan for you" or "Brightwell Lending finds the right loan for our customers."
- Must include Accreditation logos somewhere on the homepage (will try and supply these soon)
Should not have
• - Poor quality designs will not be considered
- Do not use clipart

```html
<!DOCTYPE html>
<html lang="en">
<head>
<meta charset="utf-8">
<title>Brightwell Lending – Finding the right loan for you</title>
<link href="https://fonts.googleapis.com/css2?family=Open+Sans:wght@400;600;700;800&display=swap" rel="stylesheet">
<style>
:root{
  --cyan:#2eade3;
  --cyan-dark:#1a8fc4;
  --blue:#004b70;
  --blue-deep:#0b3a55;
  --ink:#3d4a52;
  --muted:#7a8891;
  --line:#d9e3e8;
  --panel:#eef5f9;
  --white:#ffffff;
}
*{box-sizing:border-box;margin:0;padding:0}
html,body{width:1200px;height:2368px;overflow:hidden}
body{font-family:"Open Sans",Arial,sans-serif;color:var(--ink);background:var(--white);position:relative}
.page{position:relative;width:1200px;height:2368px}

/* header */
.site-header{position:absolute;left:48px;right:48px;top:36px;height:180px}
.brand{position:absolute;left:0;top:0;display:flex;align-items:center;gap:18px}
.brand-dot{width:72px;height:72px;border-radius:50%;background:var(--cyan)}
.brand-name{font-size:40px;font-weight:700;color:var(--blue);line-height:1}
.brand-tag{position:absolute;left:0;top:84px;font-size:14px;letter-spacing:1px;color:var(--blue);font-weight:600;white-space:nowrap}
.call{position:absolute;right:0;top:56px;font-size:22px;font-weight:700;color:var(--cyan)}
.search{position:absolute;right:0;top:128px;width:260px;height:36px;border:2px solid var(--line);border-radius:4px;background:var(--white)}
.search svg{position:absolute;right:8px;top:6px}

/* nav */
.main-nav{position:absolute;left:0;right:0;top:244px;height:56px;background:linear-gradient(#2a9fd6,#0f6fa3);display:flex;justify-content:center}
.main-nav ul{list-style:none;display:flex;width:1104px}
.main-nav li{flex:1;text-align:center;line-height:56px;color:var(--white);font-size:18px;font-weight:600;border-right:1px solid rgba(255,255,255,.25)}
.main-nav li:last-child{border-right:0}
.main-nav li.active{background:linear-gradient(#4fc0ee,#2eade3)}

/* hero */
.hero{position:absolute;left:48px;top:320px;width:1104px;height:440px;border-radius:6px;overflow:hidden;background:linear-gradient(160deg,#9fd2ee 0%,#c8b69a 55%,#6f8c4f 100%)}
.hero-card{position:absolute;left:0;top:40px;width:330px;height:350px;background:rgba(0,75,112,.72);padding:28px 32px;color:var(--white)}
.hero-card h2{font-size:46px;font-weight:700;color:#9fe0ff;margin-bottom:22px}
.hero-card li{list-style:none;font-size:24px;margin-bottom:16px}
.hero-card .btn{display:inline-block;margin-top:10px;background:var(--cyan);font-size:14px;padding:6px 14px;border-radius:3px}
.dots{position:absolute;left:0;right:0;top:776px;display:flex;justify-content:center;gap:10px}
.dots span{width:14px;height:14px;border-radius:50%;background:var(--line)}
.dots span.on{background:var(--cyan)}

/* welcome */
.welcome{position:absolute;left:48px;top:818px;width:1104px}
.welcome h1{font-size:26px;font-weight:700;color:var(--blue);margin-bottom:26px;text-transform:uppercase}
.welcome p{font-size:19px;line-height:1.6;margin-bottom:24px}
.welcome strong{color:var(--blue)}
.welcome .phone{color:var(--cyan);font-weight:700;font-style:italic}

/* approach */
.approach{position:absolute;left:48px;top:1362px;width:1104px;height:408px;background:var(--panel);border-radius:6px}
.approach-bar{height:60px;background:linear-gradient(#3bb6ea,#1d8fc6);color:var(--white);font-size:27px;font-weight:700;text-align:center;line-height:60px;text-transform:uppercase;border-radius:6px 6px 0 0}
.cards{display:flex;gap:28px;padding:34px 26px}
.card{flex:1;height:278px;background:var(--white);border:1px solid var(--line);border-radius:6px;padding:22px 20px;position:relative}
.card h3{font-size:30px;line-height:1.1;color:var(--cyan);font-weight:600;margin-bottom:14px}
.card li{list-style:none;font-size:14px;line-height:1.5;margin-bottom:6px;padding-left:18px;position:relative;color:var(--ink)}
.card li::before{content:"";position:absolute;left:2px;top:7px;width:7px;height:7px;border-radius:50%;background:var(--cyan)}
.card .more{position:absolute;left:20px;bottom:16px;font-size:14px;font-weight:700;color:var(--blue)}

/* calculator cta */
.borrow{position:absolute;left:392px;top:1766px;width:416px;height:120px;border-radius:10px;background:linear-gradient(#1a6d9a,#004b70);display:flex;align-items:center;gap:20px;padding:0 26px;color:var(--white)}
.borrow-text{font-size:28px;font-weight:800;line-height:1.15;text-transform:uppercase}

/* bottom boxes */
.info-row{position:absolute;left:48px;top:1960px;width:1104px;display:flex;gap:40px}
.info{flex:1;height:320px;border:1px solid var(--line);border-radius:6px;overflow:hidden;position:relative}
.info h4{height:46px;line-height:46px;padding-left:20px;background:linear-gradient(#1c79ab,#004b70);color:var(--white);font-size:17px;font-weight:700}
.info-body{padding:18px 20px;font-size:15px;line-height:1.5}
.quote{font-style:italic}
.author{margin-top:14px;text-align:right;font-weight:700;color:var(--blue)}
.author span{display:block;font-weight:400;color:var(--muted);font-size:13px}
.news-item{margin-bottom:14px}
.news-date{color:var(--cyan);font-size:13px}
.read{position:absolute;right:20px;bottom:22px;background:var(--cyan);color:var(--white);font-size:13px;padding:4px 12px;border-radius:3px}
.info-body a{color:var(--cyan)}

/* footer */
.site-footer{position:absolute;left:0;right:0;bottom:0;height:56px;background:var(--blue-deep);color:#c9dbe5;font-size:14px;display:flex;align-items:center;padding:0 48px;gap:26px}
.site-footer .spacer{flex:1}
.social{display:flex;gap:8px}
.social span{width:22px;height:22px;border-radius:3px;background:var(--cyan)}
</style>
</head>
<body>
<div class="page">

  <header class="site-header">
    <div class="brand"><div class="brand-dot"></div><div class="brand-name">Brightwell Lending</div></div>
    <div class="brand-tag">FINDING THE RIGHT LOAN FOR YOU</div>
    <div class="call">Call Us: 1800 555 210</div>
    <div class="search">
      <svg width="22" height="22" viewBox="0 0 22 22"><circle cx="9" cy="9" r="6" fill="none" stroke="#2eade3" stroke-width="2.5"/><line x1="13.5" y1="13.5" x2="19" y2="19" stroke="#2eade3" stroke-width="2.5"/></svg>
    </div>
  </header>

  <nav class="main-nav">
    <ul>
      <li class="active">HOME</li><li>SERVICES</li><li>ABOUT US</li><li>FAQ</li><li>CONTACT US</li>
    </ul>
  </nav>

  <section class="hero" role="img" aria-label="Photo of a smiling family in front of their new home">
    <div class="hero-card">
      <h2>Home Loan</h2>
      <ul><li>Home buyers</li><li>First home buyers</li><li>Over 20 lenders</li></ul>
      <span class="btn">Learn More</span>
    </div>
  </section>
  <div class="dots"><span class="on"></span><span></span><span></span></div>

  <section class="welcome">
    <h1>Welcome to Brightwell Lending</h1>
    <p>At Brightwell Lending we work hard to find the right loan for our customers. We do that because we are backed by sound industry knowledge, professional experience and a great customer service approach.</p>
    <p>Brightwell Lending guarantees that we will always tailor the best solution for your individual lending needs.</p>
    <p>We can do that because we have access to a wide variety of lending options from major banks to non-bank lenders and we are committed to finding the right lending product for you.</p>
    <p>There are many different loan products in the marketplace. Brightwell Lending has access to a wide panel of lenders which means we can access bank and non-bank lenders that meet the individual needs of our customers.</p>
    <p>Contact <strong>Brightwell Lending</strong> today on <span class="phone">1800 555 210</span> to find out more.</p>
  </section>

  <section class="approach">
    <div class="approach-bar">We offer a unique approach to help you find the right!</div>
    <div class="cards">
      <article class="card"><h3>Home Loan</h3><ul><li>Home buyers</li><li>First home buyers</li><li>Over 20 lenders</li></ul><span class="more">Learn more »</span></article>
      <article class="card"><h3>Investment Loan</h3><ul><li>Property investment loans</li><li>Interest only loans</li></ul><span class="more">Learn more »</span></article>
      <article class="card"><h3>Refinancing</h3><ul><li>Refinancing for the best rate</li><li>Upsizing or downsizing</li><li>Change from a variable to a fixed rate</li></ul><span class="more">Learn more »</span></article>
      <article class="card"><h3>Business Loan &amp; Business Finance</h3><ul><li>Long term</li><li>Short term</li><li>Equipment and Leasing</li></ul><span class="more">Learn more »</span></article>
    </div>
  </section>

  <div class="borrow">
    <svg width="64" height="64" viewBox="0 0 64 64"><circle cx="32" cy="32" r="30" fill="#2eade3"/><path d="M32 14v30M20 34l12 12 12-12" fill="none" stroke="#fff" stroke-width="6" stroke-linecap="round" stroke-linejoin="round"/></svg>
    <div class="borrow-text">Find out how much you could borrow</div>
  </div>

  <section class="info-row">
    <div class="info">
      <h4>Client testimonial</h4>
      <div class="info-body">
        <p class="quote">"Lorem ipsum dolor sit amet, consectetur adipiscing elit, sed do eiusmod tempor incididunt ut labore et dolore magna aliqua, consectetur adipiscing elit, sed do eiusmod tempor"</p>
        <p class="author">Dana Whitlow<span>Homeowner</span></p>
      </div>
    </div>
    <div class="info">
      <h4>Latest News</h4>
      <div class="info-body">
        <div class="news-item"><div class="news-date">(April 18, 2012)</div>Lorem ipsum dolor sit amet, consectetur adipiscing elit.</div>
        <div class="news-item"><div class="news-date">(April 10, 2012)</div>Lorem ipsum dolor sit amet, consectetur adipiscing elit.</div>
      </div>
      <span class="read">Read more</span>
    </div>
    <div class="info">
      <h4>Contact us</h4>
      <div class="info-body">
        <p>You can contact us by using the contact information below or by sending us a message via <a>our contact form</a>.</p>
        <p style="margin-top:14px">Brightwell Lending, CA, USA</p>
        <p style="margin-top:10px">Phone : 1800 555 210</p>
        <p style="margin-top:10px">Email: hello@brightwelllending.com</p>
      </div>
    </div>
  </section>

  <footer class="site-footer">
    <span>© 2012 Brightwell Lending</span>
    <span>home</span><span>services</span><span>about us</span><span>faq</span><span>contact us</span>
    <span class="spacer"></span>
    <span>Follow us</span>
    <div class="social"><span></span><span></span><span></span></div>
  </footer>

</div>
</body>
</html>
```